Breezeway Comfort business cards design

Need a business card design for a Heating and Air Conditioning business. I need these items included.
Business name: Breezeway Comfort
Owner: Marcus Tollefsen
License # 2874590
Phone number # 555-382-4071
Email: breezewaycomfortair@mailvista.example
Sales
Service
Installation
Maintenance

Heating and Air Conditioning

Requirements
Must have
• Company name , license number , phone number , email

```html
<!DOCTYPE html>
<html lang="en">
<head>
<meta charset="utf-8">
<title>Breezeway Comfort – Business Cards</title>
<link rel="stylesheet" href="https://fonts.googleapis.com/css2?family=Exo+2:wght@400;500;700&family=Michroma&display=swap">
<style>
  :root {
    --page-bg: #8a8a8a;
    --card-white: #ffffff;
    --brand-blue: #0a3fa8;
    --brand-blue-deep: #0a3aa8;
    --brand-orange: #f7902b;
    --brand-red: #ee4c3c;
    --ink: #1a1a1a;
    --divider: #d9d9d9;
  }
  * { margin: 0; padding: 0; box-sizing: border-box; }
  html, body { width: 1093px; height: 1200px; overflow: hidden; }
  body { background: var(--page-bg); font-family: "Exo 2", sans-serif; position: relative; }

  .card { position: absolute; left: 265px; width: 578px; height: 356px; border-radius: 26px; overflow: hidden; }
  .card--front { top: 226px; background: var(--card-white); }
  .card--back { top: 621px; background: var(--brand-blue-deep); }

  .brand-name { position: absolute; font-family: "Exo 2", sans-serif; font-weight: 700; color: var(--brand-blue); text-align: center; line-height: 1.05; }
  .card--front .brand-name { left: 22px; width: 240px; top: 120px; font-size: 40px; }
  .card--back .brand-name { left: 0; width: 578px; top: 116px; font-size: 52px; color: var(--brand-orange); }
  .brand-dot { display: block; width: 22px; height: 22px; border-radius: 50%; background: var(--brand-orange); margin: 0 auto 10px; }
  .card--back .brand-dot { width: 28px; height: 28px; }

  .divider { position: absolute; left: 278px; top: 74px; width: 1px; height: 210px; background: var(--divider); }

  .contact { position: absolute; left: 291px; right: 14px; top: 110px; color: var(--ink); }
  .contact__name { font-family: "Michroma", sans-serif; font-size: 14px; color: var(--brand-blue); letter-spacing: 0.3px; line-height: 1.2; white-space: nowrap; }
  .contact__role { font-size: 15px; color: var(--brand-red); line-height: 1.2; }
  .contact__license { margin-top: 30px; font-size: 16px; }
  .contact__license-label { color: var(--brand-blue); }
  .contact__line { display: flex; align-items: center; gap: 6px; font-size: 16px; line-height: 22px; white-space: nowrap; }
  .contact__line--phone { margin-top: 8px; }
  .contact__line--email { font-size: 13px; }
  .contact__line svg { width: 16px; height: 16px; flex: none; }

  .edge-band { position: absolute; left: 0; bottom: 0; width: 578px; height: 12px; }

  .services { position: absolute; left: 0; width: 578px; top: 310px; text-align: center; color: #fff; font-size: 17px; }
  .services__dot { display: inline-block; width: 6px; height: 6px; border-radius: 50%; background: var(--brand-orange); margin: 0 6px; vertical-align: middle; }
</style>
</head>
<body>
  <section class="card card--front">
    <div class="brand-name"><span class="brand-dot"></span>Breezeway Comfort</div>
    <div class="divider"></div>
    <div class="contact">
      <p class="contact__name">MARCUS TOLLEFSEN</p>
      <p class="contact__role">OWNER</p>
      <p class="contact__license"><span class="contact__license-label">License</span> # 2874590</p>
      <p class="contact__line contact__line--phone">
        <svg viewBox="0 0 16 16" aria-hidden="true"><path d="M4 1.5l2.2 3-1.3 1.4c.8 1.8 2.2 3.2 4 4l1.4-1.3 3 2.2-1.6 2.4C6.9 13 3 9.1 1.6 3.1z" fill="none" stroke="#ee4c3c" stroke-width="1.5" stroke-linejoin="round"/></svg>
        555-382-4071
      </p>
      <p class="contact__line contact__line--email">
        <svg viewBox="0 0 16 16" aria-hidden="true"><rect x="1" y="3" width="14" height="10" fill="#ee4c3c"/><path d="M1 3l7 5.5L15 3" fill="none" stroke="#fff" stroke-width="1.2"/></svg>
        breezewaycomfortair@mailvista.example
      </p>
    </div>
    <svg class="edge-band" viewBox="0 0 578 12" preserveAspectRatio="none" aria-hidden="true">
      <defs>
        <linearGradient id="warm-band" x1="0" x2="1">
          <stop offset="0" stop-color="#f7902b"/>
          <stop offset="1" stop-color="#ee4c3c"/>
        </linearGradient>
      </defs>
      <polygon points="0,0 282,0 276,12 0,12" fill="url(#warm-band)"/>
      <polygon points="288,0 578,0 578,12 282,12" fill="#0a3fa8"/>
    </svg>
  </section>

  <section class="card card--back">
    <div class="brand-name"><span class="brand-dot"></span>Breezeway Comfort</div>
    <p class="services">Sales<span class="services__dot"></span>Service<span class="services__dot"></span>Installation<span class="services__dot"></span>Maintenance</p>
  </section>
</body>
</html>
```